Tallowick Limited Business Card

We need a business card for a new company based in Essex, United Kingdom. We develop and manufacture educational games. The business card needs to match the company brand and logo and the colour scheme.
My company makes educational board games to be played by the family or used by teachers
The games are tile based number game

Target Market(s)

Parents, teachers, schools and children

Industry/Entity Type

Games

Contact Information for Business Card

Company Name - Tallowick Limited
Director - Damian Prouse
Registered Office - 3 Marsh Court, 142 Quarry Lane, Brindleford, Essex, CM7 4XR
Phone Number - 07950 000 318
Email - Enquiries@Tallowick.example
Website - www.Tallowick.example
Company Number - 00000000

Font styles to use
Sans Serif

Colors
00a990
ffffff

Requirements
Must have
• Same colour scheme as the attachments - green and white
• Same font style for Tallowick
• Images of the number tiles similar to the attachments
• extra details
• The colour is Cyan - 82 Magenta - 24 Yellow - 44 Black - 2
• I have attached some of the font styles use on my website and alos my LOGO
Nice to have
• Image of the number "1" tag as seen on the website

```html
<!DOCTYPE html>
<html lang="en">
<head>
<meta charset="utf-8">
<title>Tallowick Limited – Business Card</title>
<link rel="stylesheet" href="https://fonts.googleapis.com/css2?family=Jost:wght@400;500;600&display=swap">
<style>
  :root {
    --brand: #4fae97;
    --brand-deep: #3f9c85;
    --paper: #f4f5f3;
    --ink: #3a3d3f;
    --ink-soft: #55595b;
    --tile-wash-a: #e6ebe8;
    --tile-wash-b: #d5e2dc;
    --backdrop: #e9ecea;
  }
  * { box-sizing: border-box; margin: 0; padding: 0; }
  html, body { width: 1200px; height: 800px; overflow: hidden; }
  body {
    background: var(--backdrop);
    font-family: "Jost", "Futura", sans-serif;
    display: flex;
    align-items: center;
    justify-content: center;
    gap: 60px;
  }
  .card {
    width: 540px;
    height: 309px;
    position: relative;
    overflow: hidden;
    box-shadow: 0 6px 18px rgba(0,0,0,.12);
  }

  /* Front */
  .card-front {
    background: var(--brand);
    display: flex;
    align-items: center;
    justify-content: center;
  }
  .brand-lockup { text-align: center; color: #fff; }
  .brand-name {
    font-weight: 600;
    font-size: 64px;
    letter-spacing: -1px;
    line-height: 1;
  }
  .brand-tagline {
    margin-top: 6px;
    font-weight: 400;
    font-size: 13px;
    letter-spacing: 1.2px;
  }

  /* Back */
  .card-back { background: var(--paper); }
  .side-strip {
    position: absolute; left: 0; top: 0; bottom: 0;
    width: 24px; background: var(--brand);
  }
  .tile-backdrop {
    position: absolute; left: 24px; top: 0; right: 0; bottom: 0;
    background: radial-gradient(ellipse at 55% 60%, var(--tile-wash-b) 0%, var(--tile-wash-a) 45%, var(--paper) 85%);
    opacity: .9;
  }
  .holder { position: absolute; left: 24px; right: 0; top: 0; bottom: 0; color: var(--ink); }
  .person { position: absolute; top: 52px; left: 0; right: 0; text-align: center; padding-left: 40px; }
  .person-name { font-size: 27px; font-weight: 400; letter-spacing: .5px; line-height: 1; }
  .person-role { font-size: 16px; color: var(--ink-soft); margin-top: 4px; }
  .role-rule { width: 18px; height: 3px; background: var(--brand); margin: 3px auto 0; }

  .contact-list { position: absolute; left: 14px; top: 190px; list-style: none; }
  .contact-list li {
    display: flex; align-items: center; gap: 10px;
    font-size: 13px; letter-spacing: .3px; color: var(--ink);
    height: 26px;
  }
  .contact-list svg { width: 18px; height: 18px; flex: none; }

  .company {
    position: absolute; right: 26px; top: 184px;
    width: 230px;
    text-align: right; font-size: 12.5px; letter-spacing: .3px;
  }
  .company-id {
    border-right: 3px solid var(--brand);
    padding-right: 6px;
    line-height: 1.35;
  }
  .company-pin {
    height: 18px;
    margin-top: 4px;
    padding-left: 116px;
    text-align: left;
  }
  .company-pin svg { width: 14px; height: 18px; display: block; }
  .company-address { margin-top: 2px; line-height: 1.35; }
</style>
</head>
<body>

  <section class="card card-front" aria-label="Card front">
    <div class="brand-lockup">
      <div class="brand-name">Tallowick</div>
      <div class="brand-tagline">THE EDUCATIONAL GAME COMPANY</div>
    </div>
  </section>

  <section class="card card-back" aria-label="Card back">
    <div class="side-strip"></div>
    <div class="tile-backdrop" role="img" aria-label="Faint photograph of scattered numbered game tiles and the boxed tile game"></div>
    <div class="holder">
      <div class="person">
        <div class="person-name">DAMIAN PROUSE</div>
        <div class="person-role">Director</div>
        <div class="role-rule"></div>
      </div>

      <ul class="contact-list">
        <li>
          <svg viewBox="0 0 18 18"><rect x="5" y="1" width="8" height="16" rx="1.5" fill="none" stroke="var(--brand)" stroke-width="1.6"/><line x1="8" y1="14.5" x2="10" y2="14.5" stroke="var(--brand)" stroke-width="1.4"/></svg>
          07950 000 318
        </li>
        <li>
          <svg viewBox="0 0 18 18"><rect x="1" y="4" width="16" height="11" fill="var(--brand)"/><polyline points="1,4 9,10 17,4" fill="none" stroke="#fff" stroke-width="1.2"/></svg>
          ENQUIRIES@TALLOWICK.EXAMPLE
        </li>
        <li>
          <svg viewBox="0 0 18 18" fill="none" stroke="var(--brand)" stroke-width="1.2"><circle cx="9" cy="9" r="7.5"/><ellipse cx="9" cy="9" rx="3.2" ry="7.5"/><line x1="1.5" y1="9" x2="16.5" y2="9"/><line x1="3" y1="5" x2="15" y2="5"/><line x1="3" y1="13" x2="15" y2="13"/></svg>
          WWW.TALLOWICK.EXAMPLE
        </li>
      </ul>

      <div class="company">
        <div class="company-id">TALLOWICK LIMITED<br>COMPANY NUMBER - 00000000</div>
        <div class="company-pin">
          <svg viewBox="0 0 14 18"><path d="M7 17 C3 11 1 9 1 6.5 A6 6 0 0 1 13 6.5 C13 9 11 11 7 17Z" fill="var(--brand)"/><circle cx="7" cy="6.5" r="2.2" fill="#fff"/></svg>
        </div>
        <div class="company-address">3 MARSH COURT, 142 QUARRY LANE,<br>BRINDLEFORD, ESSEX, CM7 4XR</div>
      </div>
    </div>
  </section>

</body>
</html>
```